Business Card for Makeup Artist

I need a business card designed for my makeup and hair artistry business which is primarily events and weddings focused. The card needs to be sleek, simple, stylish and appealing to women. I would prefer a white background but open to suggestions also. I also love the marble background look. I have attached some example pics. It needs to be a double sided card with logo and/or design on one side and contact details in the centre of the card on the other side. NO LOGO ON BACK. Examples attached.

Target Market(s)

Females age 14-55

Industry/Entity Type

Business

Contact Information for Business Card

Nora Vint
Principal Makeup Artist
P: 0413 925 214
E: nora@lumirabeauty.com.au
W: www.lumirabeauty.com.au

Requirements
Should not have
• No yellow, green, red or blue in the design.

```html
<!DOCTYPE html>
<html lang="en">
<head>
<meta charset="utf-8">
<title>Lumira Makeup Artistry – Business Card</title>
<link href="https://fonts.googleapis.com/css2?family=Quicksand:wght@400;500&display=swap" rel="stylesheet">
<style>
  :root {
    --page-bg: #ffffff;
    --card-dark: #161616;
    --card-deep: #0e0e0e;
    --card-tone: #1f2222;
    --ink: #f4f4f4;
    --ink-soft: #d9d9d9;
    --rule: #bdbdbd;
  }
  * { margin: 0; padding: 0; box-sizing: border-box; }
  html, body {
    width: 1200px;
    height: 1200px;
    overflow: hidden;
    background: var(--page-bg);
  }
  .canvas {
    position: relative;
    width: 1200px;
    height: 1200px;
    background: var(--page-bg);
    font-family: "Quicksand", "Helvetica Neue", Arial, sans-serif;
    color: var(--ink);
  }
  .card {
    position: absolute;
    left: 120px;
    width: 960px;
    height: 590px;
    overflow: hidden;
  }
  .card--back { top: 4px; }
  .card--front { top: 606px; }
  .card__pattern {
    position: absolute;
    inset: 0;
    background:
      radial-gradient(ellipse at 40% 30%, var(--card-tone) 0%, transparent 70%),
      linear-gradient(160deg, var(--card-dark) 0%, var(--card-deep) 100%);
  }
  .holder {
    position: absolute;
    left: 52px;
    top: 50px;
  }
  .holder__name {
    font-size: 32px;
    font-weight: 500;
    letter-spacing: 1px;
    text-transform: lowercase;
    line-height: 1;
  }
  .holder__title {
    margin-top: 12px;
    font-size: 21px;
    font-weight: 400;
    letter-spacing: 1px;
    text-transform: uppercase;
    color: var(--ink-soft);
    line-height: 1;
  }
  .contact {
    position: absolute;
    left: 440px;
    top: 380px;
    height: 108px;
  }
  .contact__rule {
    position: absolute;
    left: 38px;
    top: 0;
    width: 2px;
    height: 108px;
    background: var(--rule);
  }
  .contact__row {
    position: absolute;
    left: 0;
    height: 30px;
    display: flex;
    align-items: center;
  }
  .contact__row:nth-of-type(1) { top: 8px; }
  .contact__row:nth-of-type(2) { top: 41px; }
  .contact__row:nth-of-type(3) { top: 74px; }
  .contact__icon {
    width: 26px;
    height: 26px;
    margin-left: 4px;
    fill: var(--ink);
  }
  .contact__text {
    position: absolute;
    left: 50px;
    font-size: 26px;
    font-weight: 400;
    white-space: nowrap;
    letter-spacing: 0.3px;
    line-height: 1;
  }
  .brand {
    position: absolute;
    left: 0;
    right: 0;
    top: 210px;
    text-align: center;
  }
  .brand__name {
    font-size: 118px;
    font-weight: 500;
    line-height: 1;
    color: var(--ink);
    letter-spacing: 2px;
  }
  .brand__tagline {
    margin-top: 16px;
    margin-left: 60px;
    font-size: 32px;
    font-weight: 400;
    letter-spacing: 1.5px;
    text-transform: uppercase;
    color: var(--ink-soft);
    line-height: 1;
  }
</style>
</head>
<body>
<main class="canvas">

  <section class="card card--back">
    <div class="card__pattern" role="img" aria-label="Dark charcoal floral lace pattern background"></div>

    <div class="holder">
      <p class="holder__name">nora vint</p>
      <p class="holder__title">Principal Makeup Artist</p>
    </div>

    <div class="contact">
      <span class="contact__rule"></span>
      <div class="contact__row">
        <svg class="contact__icon" viewBox="0 0 24 24" aria-hidden="true">
          <path d="M6.6 10.8a15.1 15.1 0 0 0 6.6 6.6l2.2-2.2c.3-.3.7-.4 1-.2 1.1.4 2.3.6 3.6.6.6 0 1 .4 1 1V20c0 .6-.4 1-1 1A17 17 0 0 1 3 4c0-.6.4-1 1-1h3.5c.6 0 1 .4 1 1 0 1.3.2 2.5.6 3.6.1.3 0 .7-.2 1z"/>
        </svg>
        <span class="contact__text">0413 925 214</span>
      </div>
      <div class="contact__row">
        <svg class="contact__icon" viewBox="0 0 24 24" aria-hidden="true">
          <path d="M2 5h20v14H2z" fill="none" stroke="#f4f4f4" stroke-width="2"/>
          <path d="M2 5l10 8 10-8" fill="none" stroke="#f4f4f4" stroke-width="2"/>
        </svg>
        <span class="contact__text">nora@lumirabeauty.com.au</span>
      </div>
      <div class="contact__row">
        <svg class="contact__icon" viewBox="0 0 24 24" aria-hidden="true">
          <g fill="none" stroke="#f4f4f4" stroke-width="1.8">
            <circle cx="12" cy="12" r="9.5"/>
            <ellipse cx="12" cy="12" rx="4.2" ry="9.5"/>
            <path d="M2.5 12h19M4 7h16M4 17h16"/>
          </g>
        </svg>
        <span class="contact__text">lumirabeauty.com.au</span>
      </div>
    </div>
  </section>

  <section class="card card--front">
    <div class="card__pattern" role="img" aria-label="Dark charcoal floral lace pattern background"></div>

    <div class="brand">
      <p class="brand__name">Lumira</p>
      <p class="brand__tagline">Makeup Artistry</p>
    </div>
  </section>

</main>
</body>
</html>
```